New Web Design Project

Require a website for The Bramwell Harvest. All relevant information is in the uploaded files.

website to be responsive to work on mobile.

Required in html5, css

Coding

Coded - Design and coding required

Number of Pages Required

3 page

```html
<!DOCTYPE html>
<html lang="en">
<head>
<meta charset="utf-8">
<title>The Bramwell Harvest</title>
<link href="https://fonts.googleapis.com/css2?family=Poppins:wght@400;500;600;700&family=Montserrat:wght@400;500;600&family=Lora:wght@600;700&display=swap" rel="stylesheet">
<style>
:root{
  --green:#9bcb34;
  --orange:#fd9a37;
  --orange-deep:#f7931e;
  --ink:#111;
  --body:#666;
  --white:#fff;
  --black:#000;
  --link:#1565c0;
}
*{box-sizing:border-box;margin:0;padding:0}
html,body{width:1200px;height:3109px;overflow:hidden}
body{position:relative;font-family:"Montserrat",sans-serif;color:var(--body);background:var(--white)}
.abs{position:absolute}
.btn{position:absolute;background:var(--orange);color:var(--white);font-family:"Poppins",sans-serif;font-weight:600;font-size:15px;letter-spacing:.5px;display:flex;align-items:center;justify-content:center;border-radius:2px}

/* hero */
.hero{position:absolute;left:0;top:0;width:1200px;height:637px;background:linear-gradient(135deg,#6d6a68 0%,#4f5256 40%,#3b4046 70%,#5d6266 100%)}
.hero-shade{position:absolute;inset:0;background:rgba(20,20,20,.35)}
.hero-curve{position:absolute;left:0;top:0}
.logo{position:absolute;display:flex;flex-direction:column;align-items:center;font-family:"Poppins",sans-serif;font-weight:700;text-align:center;line-height:1.05}
.logo-dot{width:30px;height:30px;border-radius:50%;background:var(--green);margin-bottom:6px}
.logo-header{left:46px;top:14px;width:160px;font-size:22px;color:#3a3a3a}
.nav{position:absolute;top:14px;left:640px;font-size:12.5px;color:var(--white);font-family:"Montserrat",sans-serif;font-weight:500}
.nav span{position:absolute;white-space:nowrap}
.nav .active{color:var(--orange)}
.hero-title{position:absolute;top:260px;left:0;width:1200px;text-align:center;font-family:"Poppins",sans-serif;font-weight:700;font-size:36px;letter-spacing:2px;color:var(--green)}
.hero-text{position:absolute;top:313px;left:300px;width:600px;text-align:center;color:var(--white);font-size:12.5px;line-height:19.5px;font-weight:500}

/* tagline band */
.band{position:absolute;left:0;top:637px;width:1200px;height:83px;background:var(--green)}
.band-text{position:absolute;left:62px;top:24px;font-family:"Lora",serif;font-weight:700;font-size:23px;color:var(--ink)}

/* about */
.about-photo{position:absolute;left:62px;top:795px;width:449px;height:375px;background:linear-gradient(135deg,#c9c2b6,#8f8a80 45%,#5d5a55)}
.eyebrow{position:absolute;font-family:"Poppins",sans-serif;font-weight:600;font-size:14px;color:var(--orange);letter-spacing:.3px}
.section-title{position:absolute;font-family:"Poppins",sans-serif;font-weight:500;color:var(--ink)}
.section-title em{font-style:normal;color:var(--green)}
.about-title{left:590px;top:822px;width:420px;font-size:29px;line-height:38px}
.about-copy{position:absolute;left:590px;top:905px;width:440px;font-size:12px;line-height:19.5px;color:#666}
.about-copy p{margin-bottom:10px}

/* partners */
.partners{position:absolute;left:0;top:1298px;width:1200px;height:456px;background:var(--orange)}
.partners .eyebrow{color:var(--white);top:80px;left:0;width:1200px;text-align:center}
.partners-title{top:102px;left:0;width:1200px;text-align:center;font-size:32px}
.partners-title em{color:var(--white);font-style:normal}
.portrait{position:absolute;width:188px;height:188px;border-radius:50%;background:#fbb873;display:flex;align-items:center;justify-content:center}
.portrait div{width:164px;height:164px;border-radius:50%;background:radial-gradient(circle at 50% 40%,#8a8f98,#3c4049 70%)}
.card{position:absolute;width:304px;height:217px;background:var(--white);border-radius:6px;padding:24px 16px 0 31px}
.card::before{content:"";position:absolute;left:-12px;top:46px;border-right:12px solid var(--white);border-top:11px solid transparent;border-bottom:11px solid transparent}
.card h3{font-family:"Lora",serif;font-weight:600;font-size:17px;line-height:22px;color:var(--ink)}
.card .role{font-size:11px;line-height:14px;color:var(--orange);margin-top:3px}
.card p.bio{font-size:11px;line-height:18.5px;color:#666;margin-top:10px;letter-spacing:-.1px}
.card a{display:block;color:var(--link);text-decoration:none;font-size:15.5px;line-height:23px;margin-top:3px;white-space:nowrap}

/* social */
.social .eyebrow{top:1836px;left:0;width:1200px;text-align:center}
.social-title{top:1862px;left:0;width:1200px;text-align:center;font-size:34px}
.net{position:absolute;top:1925px;width:250px;text-align:center}
.net svg{display:block;margin:0 auto}
.net-url{font-size:16px;line-height:22px;color:var(--ink);margin-top:18px;font-family:"Montserrat",sans-serif;white-space:nowrap}

/* contact */
.contact{position:absolute;left:0;top:2205px;width:1200px;height:600px;background:linear-gradient(120deg,#3d4043 0%,#4d5054 35%,#5a5d61 60%,#3f4246 100%)}
.contact-shade{position:absolute;inset:0;background:rgba(40,40,40,.35)}
.contact-title{position:absolute;left:600px;top:74px;width:565px;text-align:center;font-family:"Poppins",sans-serif;font-weight:500;font-size:30px;color:var(--orange)}
.contact-text{position:absolute;left:628px;top:119px;width:510px;text-align:center;color:var(--white);font-size:12px;line-height:18px}
.contact-ask{position:absolute;left:600px;top:160px;width:565px;text-align:center;color:var(--white);font-size:11.5px;font-weight:600}
.field{position:absolute;left:706px;width:389px;height:31px;background:var(--white);border:1px solid #cfcfcf;font-size:12px;color:#777;padding:8px 10px}
.field.first{border-color:var(--green)}

/* footer */
.footer{position:absolute;left:0;top:2790px;width:1200px;height:285px;background:var(--black)}
.logo-footer{left:58px;top:30px;width:140px;font-size:24px;color:var(--white)}
.footer-about{position:absolute;left:62px;top:165px;width:260px;color:var(--white);font-size:12px;line-height:19.5px}
.f-col{position:absolute;top:34px}
.f-col h4{font-family:"Poppins",sans-serif;font-weight:500;font-size:14px;color:var(--orange);margin-bottom:8px}
.f-col li{list-style:none;color:var(--white);font-size:12px;line-height:34px}
.loc{position:absolute;left:888px;display:flex;gap:14px;color:var(--white);font-size:12px;line-height:19px}
.loc svg{flex:none}
.copyright{position:absolute;left:0;top:3075px;width:1200px;height:34px;background:var(--orange);color:var(--white);font-size:12px;display:flex;align-items:center;justify-content:center}
</style>
</head>
<body>

<header class="hero">
  <div class="hero-photo abs" style="inset:0" role="img" aria-label="Photo of three colleagues reviewing work at a laptop in a bright office"></div>
  <div class="hero-shade"></div>
  <svg class="hero-curve" width="600" height="160" viewBox="0 0 600 160">
    <path d="M0 0 H488 C420 70 270 130 0 143 Z" fill="#fff"/>
    <path d="M488 0 C420 70 270 130 0 143" fill="none" stroke="#fd9a37" stroke-width="3"/>
  </svg>
  <div class="logo logo-header"><span class="logo-dot"></span>The Bramwell Harvest</div>
  <nav class="nav">
    <span class="active" style="left:24px">HOME</span>
    <span style="left:92px">ABOUT US</span>
    <span style="left:184px">PEOPLE</span>
    <span style="left:258px">SOCIAL MEDIA</span>
    <span style="left:377px">CONTACT US</span>
  </nav>
  <svg class="abs" style="left:1121px;top:13px" width="18" height="18" viewBox="0 0 18 18"><circle cx="7" cy="7" r="5.5" fill="none" stroke="#9bcb34" stroke-width="2"/><path d="M11 11 L16.5 16.5" stroke="#9bcb34" stroke-width="2.4" stroke-linecap="round"/></svg>
  <h1 class="hero-title">THE BRAMWELL HARVEST COMPANY</h1>
  <p class="hero-text">Lorem Ipsum is simply dummy text of the printing and typesetting industry. Lorem Ipsum has been the industry's standard dummy text ever since the 1500s, when an unknown printer took a galley of type and scrambled it to make a type specimen book.</p>
  <span class="btn" style="left:525px;top:389px;width:150px;height:43px">CONTACT US</span>
</header>

<section class="band">
  <p class="band-text">Doing The Right Thing, At Right Time</p>
  <span class="btn" style="left:990px;top:26px;width:149px;height:35px">GET STARTED</span>
</section>

<section class="about">
  <div class="about-photo" role="img" aria-label="Photo of a young team gathered around a laptop at a wooden table"></div>
  <p class="eyebrow" style="left:590px;top:800px">ABOUT US</p>
  <h2 class="section-title about-title">Your Success Is <em>Our Only Business</em></h2>
  <div class="about-copy">
    <p>The Bramwell Harvest Company was incorporated with the objective of introduo the Canadian market through a trusted and mutual business relation</p>
    <p>It was set up by Omar Castellane and Nico Varelis who have combined experience of over 45 years in the fresh produce business. With Omar's expertise in global sourcing and Nico's vast connection and know how of the Canadian market, we have helped our existing partners grow and expand their reach in the Canadian fresh produce market</p>
    <p>Our expertise and supply chain knowledge allow us to develop programs and introduce new products to the Canadian consumer, via retail and wholesale channels across Canada.</p>
    <p>Get in touch to discuss how we can add value to your business</p>
  </div>
</section>

<section class="partners">
  <p class="eyebrow">PEOPLE</p>
  <h2 class="section-title partners-title">Our <em>Partner</em></h2>
  <div class="portrait" style="left:59px;top:169px"><div role="img" aria-label="Portrait photo of Omar Castellane"></div></div>
  <article class="card" style="left:280px;top:170px">
    <h3>Omar Castellane</h3>
    <p class="role">Founder &amp; President</p>
    <p class="bio">Lorem Ipsum is simply dummy text of the printing and typesetting industry. Lorem Ipsum has been the industry's standard dummy text ever since the 1500s, when an unknown printer took a</p>
    <a>https://www.worknet.example/in/<br>omar-castellane-41c7/</a>
  </article>
  <div class="portrait" style="left:614px;top:169px"><div role="img" aria-label="Portrait photo of Nico Varelis"></div></div>
  <article class="card" style="left:835px;top:170px">
    <h3>Nico Varelis</h3>
    <p class="role">Founder</p>
    <p class="bio">Lorem Ipsum is simply dummy text of the printing and typesetting industry. Lorem Ipsum has been the industry's standard dummy text ever since the 1500s, when an unknown printer took a</p>
    <a>https://www.worknet.example/in/<br>nico-varelis-58d2/</a>
  </article>
</section>

<section class="social">
  <p class="eyebrow">JOIN US</p>
  <h2 class="section-title social-title">Social <em>Media Links</em></h2>
  <svg width="0" height="0" style="position:absolute">
    <defs>
      <linearGradient id="hexFill" x1="0" y1="0" x2="0" y2="1"><stop offset="0" stop-color="#9bcb34"/><stop offset="1" stop-color="#f7931e"/></linearGradient>
    </defs>
  </svg>
  <div class="net" style="left:62px">
    <svg width="150" height="150" viewBox="0 0 150 150"><polygon points="75,4 144,40 144,110 75,146 6,110 6,40" fill="#bbb" transform="translate(4,4)"/><polygon points="75,4 144,40 144,110 75,146 6,110 6,40" fill="url(#hexFill)"/><circle cx="75" cy="75" r="22" fill="none" stroke="#fff" stroke-width="5"/></svg>
    <p class="net-url">https://www.circlely.example<br>/bramwellharvest</p>
  </div>
  <div class="net" style="left:336px">
    <svg width="150" height="150" viewBox="0 0 150 150"><polygon points="75,4 144,40 144,110 75,146 6,110 6,40" fill="#bbb" transform="translate(4,4)"/><polygon points="75,4 144,40 144,110 75,146 6,110 6,40" fill="url(#hexFill)"/><circle cx="75" cy="75" r="22" fill="none" stroke="#fff" stroke-width="5"/></svg>
    <p class="net-url">https://chatterly.example/<br>bramwellharvest</p>
  </div>
  <div class="net" style="left:611px">
    <svg width="150" height="150" viewBox="0 0 150 150"><polygon points="75,4 144,40 144,110 75,146 6,110 6,40" fill="#bbb" transform="translate(4,4)"/><polygon points="75,4 144,40 144,110 75,146 6,110 6,40" fill="url(#hexFill)"/><circle cx="75" cy="75" r="22" fill="none" stroke="#fff" stroke-width="5"/></svg>
    <p class="net-url">https://worknet.example/<br>company/bramwell-harvest</p>
  </div>
  <div class="net" style="left:886px">
    <svg width="150" height="150" viewBox="0 0 150 150"><polygon points="75,4 144,40 144,110 75,146 6,110 6,40" fill="#bbb" transform="translate(4,4)"/><polygon points="75,4 144,40 144,110 75,146 6,110 6,40" fill="url(#hexFill)"/><circle cx="75" cy="75" r="22" fill="none" stroke="#fff" stroke-width="5"/></svg>
    <p class="net-url">https://www.picturely.example<br>/bramwellharvest</p>
  </div>
</section>

<section class="contact">
  <div class="abs" style="inset:0" role="img" aria-label="Photo of two smiling businessmen in suits talking at a desk"></div>
  <div class="contact-shade"></div>
  <h2 class="contact-title">CONTACT US</h2>
  <p class="contact-text">Lorem Ipsum is simply dummy text of the printing and typesetting industry. Lorem Ipsum has been the industry's standard dummy text ever</p>
  <p class="contact-ask">Need An have Question Please Contact Us.</p>
  <div class="field first" style="top:190px">Name *</div>
  <div class="field" style="top:229px">Email *</div>
  <div class="field" style="top:268px">Phone *</div>
  <div class="field" style="top:308px;height:67px">Message *</div>
  <span class="btn" style="left:839px;top:390px;width:119px;height:37px">SUBMIT</span>
</section>

<svg class="abs" style="left:0;top:2680px" width="1200" height="112" viewBox="0 0 1200 112">
  <path d="M0 32 C250 -5 520 20 760 62 C950 95 1100 110 1200 104 V112 H0 Z" fill="#000"/>
  <path d="M0 32 C250 -5 520 20 760 62 C950 95 1100 110 1200 104" fill="none" stroke="#fd9a37" stroke-width="3"/>
</svg>

<footer class="footer">
  <div class="logo logo-footer"><span class="logo-dot"></span>The Bramwell Harvest</div>
  <p class="footer-about">Our expertise and supply chain knowledge allow us to develop programs and introduce products to the Canadian consumer, via retail and</p>
  <div class="f-col" style="left:338px">
    <h4>USE FULL LINK</h4>
    <ul><li>- Home</li><li>- About Us</li><li>- People</li><li>- Social media</li><li>- Contact us</li></ul>
  </div>
  <div class="f-col" style="left:613px">
    <h4>PRIVACY POLICE</h4>
    <ul><li>- Links</li><li>- Privacy</li><li>- Location</li></ul>
  </div>
  <div class="f-col" style="left:888px"><h4>LOCATION</h4></div>
  <div class="loc" style="top:65px">
    <svg width="20" height="26" viewBox="0 0 20 26"><path d="M10 1 C4.5 1 1 5 1 10 C1 16 10 25 10 25 C10 25 19 16 19 10 C19 5 15.5 1 10 1 Z" fill="#fff"/><circle cx="10" cy="10" r="3.5" fill="#000"/></svg>
    <span style="width:190px">Lorem Ipsum is simply dummy text of the printing</span>
  </div>
  <div class="loc" style="top:128px">
    <svg width="20" height="20" viewBox="0 0 24 24"><path d="M6.6 10.8c1.4 2.8 3.8 5.1 6.6 6.6l2.2-2.2c.3-.3.7-.4 1-.2 1.1.4 2.3.6 3.6.6.6 0 1 .4 1 1V20c0 .6-.4 1-1 1C10.6 21 3 13.4 3 4c0-.6.4-1 1-1h3.5c.6 0 1 .4 1 1 0 1.3.2 2.5.6 3.6.1.3 0 .7-.2 1L6.6 10.8z" fill="#fff"/></svg>
    <span>123 456 7890</span>
  </div>
  <div class="loc" style="top:186px">
    <svg width="24" height="18" viewBox="0 0 24 18"><rect x="0" y="1" width="24" height="16" fill="#fff"/><path d="M0 1 L12 10 L24 1" fill="none" stroke="#000" stroke-width="2"/></svg>
    <span>info@bramwellharvest.com</span>
  </div>
</footer>

<p class="copyright">© Bramwellharvestcompany . 2020- All Right Reserved</p>

</body>
</html>
```